BRAVEWELL DISPLAY GROUP Website

Looking for a website design that clearly and powerfully portrays our unique and effective indoor advertising billboards in our network.

Our TinyPlates, TallPlates and GrandFlags are strategically placed in high traffic areas of restaurants, pubs, nightclubs, fitness clubs, colleges and universities, and sports arenas.

Bravewell Display Group is our new name. Our current site is www.plovacorp.ca with our focus now being entirely on our Out-of-Home media. New website address will be www.bravewelldisplay.ca

We need the following sections:

HOME
PRODUCTS (Drop down menu)
-TinyPlates
-TallPlates
-GrandFlags
NETWORKS (Drop down menu)
-Dine-Pour
-Sports
-Campus
EFFECTIVENESS
CAMPAIGNS *This page will show numerous ad campaigns and could be a slide show (see www.plovacorp.ca/KVPL_campaigns.html )
BECOME A PARTNER
CONTACT

Please include social media functions on the homepage such as chirpnet/pagelink/workring

We will be supplying content and photos as required.

Our plan is to have you submit the homepage design to start with, and then we can start judging which styles we like the best and can start narrowing our list. As a second round, we would like to ask the "finalists" to submit a second page (another section of the website) and to see how consistent you are in terms of the look and feel you proposed for the homepage.

Attached is our new logo.

We may require you to upload the final website for us.

Websites that are in similar industry are:
www.torvelix.com
www.quandrafeed.com

Industry/Entity Type

Advertising

Requirements
Must have
• Our network offers advertising solutions that feature: Guaranteed Readership,100% Gender Specific, Frequency, and Captive Audience. Purchasing advertising space in our network are small to medium business owners and advertising agencies booking on behalf of their clients.

Site must be professional and modern looking.
Nice to have
• Moving banner or slide show of some type.

```html
<!DOCTYPE html>
<html lang="en">
<head>
<meta charset="utf-8">
<title>Bravewell Display Group</title>
<link href="https://fonts.googleapis.com/css2?family=Bebas+Neue&family=Cinzel:wght@400&family=Arimo:wght@400;700&family=Tinos&display=swap" rel="stylesheet">
<style>
:root{
  --brand-blue:#12339a;
  --nav-top:#2b2b2b;
  --nav-bottom:#000;
  --accent-yellow:#fcc628;
  --text:#111;
  --muted:#bdbdbd;
  --frame:#d6d6d6;
  --thumb-border:#c4c4c4;
}
*{margin:0;padding:0;box-sizing:border-box}
html,body{width:1200px;height:962px;overflow:hidden;background:#fff;font-family:Arimo,Arial,sans-serif;color:var(--text)}
.page{position:relative;width:1200px;height:962px}
.top-band{position:absolute;left:0;top:0;width:1200px;height:253px;background:var(--brand-blue)}
.brand{position:absolute;left:132px;top:14px;display:flex;align-items:center;gap:10px;color:#fff;font-family:Arimo,Arial,sans-serif;font-weight:700;font-size:19px;line-height:1.1;width:190px}
.brand-mark{width:36px;height:36px;background:#fff;border-radius:6px;flex:none}
.social{position:absolute;left:972px;top:12px;display:flex;gap:2px}
.social span{width:30px;height:31px;border-radius:6px;display:block}
.social .workring{background:#3d8fc6}
.social .chirpnet{background:#5cc3e0}
.social .feed{background:#e9742d}
.main-nav{position:absolute;left:328px;top:46px;width:737px;height:44px;background:linear-gradient(var(--nav-top),var(--nav-bottom));border-radius:5px 5px 0 0;display:flex}
.main-nav a{color:#fff;text-decoration:none;font-family:Arimo,Arial,sans-serif;font-weight:700;font-size:15.5px;display:flex;align-items:center;justify-content:center;border-left:1px solid #444;letter-spacing:-.2px}
.main-nav a:first-child{border-left:none}
.hero-frame{position:absolute;left:131px;top:90px;width:935px;height:322px;background:#fff;border:1px solid var(--frame);border-top:none}
.hero{position:absolute;left:10px;top:12px;width:914px;height:296px;background:linear-gradient(90deg,#3a3d44 0%,#8a93a0 35%,#d9dde3 60%,#c9ccd0 100%)}
.hero-title{position:absolute;left:26px;top:18px;font-family:"Bebas Neue",sans-serif;font-size:88px;line-height:1;color:var(--accent-yellow)}
.hero-points{position:absolute;left:31px;top:114px;list-style:none;font-family:Tinos,"Times New Roman",serif;font-size:23px;line-height:36px;color:#fff}
.hero-points li:last-child{padding-left:5px}
.read-more{position:absolute;left:286px;top:254px;width:143px;height:42px;background:var(--accent-yellow);border-top:4px solid #fff;font-family:Arimo,Arial,sans-serif;font-size:20px;color:#111;display:flex;align-items:center;justify-content:center;text-decoration:none}
.section-title{position:absolute;font-family:Cinzel,serif;font-size:31px;font-weight:400;color:#111;letter-spacing:.5px}
.copy{position:absolute;left:133px;width:491px;font-size:14px;line-height:22px;text-align:justify}
.divider{position:absolute;left:672px;top:446px;width:1px;height:404px;background:#d0d0d0}
.offer{position:absolute;left:705px;width:360px;height:100px}
.offer-thumb{position:absolute;left:0;top:0;width:103px;height:99px;border:3px solid var(--thumb-border);border-radius:3px;background:linear-gradient(135deg,#e4e7ea,#9aa3ad)}
.offer h3{position:absolute;left:111px;top:0;font-size:14px;font-weight:700}
.offer p{position:absolute;left:111px;top:20px;width:247px;font-size:12px;line-height:18px;text-align:justify}
.footer{position:absolute;left:0;top:895px;width:1200px;height:67px;background:linear-gradient(#2a2a2a,#000)}
.footer-links{position:absolute;left:139px;top:25px;font-size:12px;color:var(--muted)}
.footer-links a{color:var(--muted);text-decoration:none}
.footer-links .sep{margin:0 10px}
.copyright{position:absolute;right:132px;top:23px;font-size:12px;color:var(--muted)}
</style>
</head>
<body>
<div class="page">
  <div class="top-band"></div>
  <div class="brand"><span class="brand-mark"></span>Bravewell Display Group</div>
  <div class="social">
    <span class="workring" role="img" aria-label="workring"></span>
    <span class="chirpnet" role="img" aria-label="chirpnet"></span>
    <span class="feed" role="img" aria-label="news feed"></span>
  </div>
  <nav class="main-nav">
    <a href="#" style="width:76px">HOME</a>
    <a href="#" style="width:107px">PRODUCTS</a>
    <a href="#" style="width:109px">NETWORKS</a>
    <a href="#" style="width:145px">EFFECTIVENESS</a>
    <a href="#" style="width:175px">BECOME A PARTNER</a>
    <a href="#" style="width:125px">CONTACT US</a>
  </nav>

  <div class="hero-frame">
    <div class="hero" role="img" aria-label="Smiling businessman in a bright office">
      <div class="hero-title">WE OFFERS</div>
      <ul class="hero-points">
        <li>Guaranteed Readership</li>
        <li>100% Gender Specific</li>
        <li>Frequency, and Captive Audience.</li>
      </ul>
      <a class="read-more" href="#">Read More...</a>
    </div>
  </div>

  <h2 class="section-title" style="left:131px;top:440px">We Work for You!</h2>
  <p class="copy" style="top:484px">Lorem Ipsum is simply dummy text of the printing and typesetting industry. Lorem Ipsum has been the industry's standard dummy text ever since the 1500s, when an unknown printer took a galley of type and scrambled it to make a type specimen book. It has survived not only five centuries, but also the leap into electronic typesetting, remaining essentially unchanged.</p>

  <h2 class="section-title" style="left:131px;top:637px">Advertising Solutions</h2>
  <p class="copy" style="top:705px">Lorem Ipsum is simply dummy text of the printing and typesetting industry. Lorem Ipsum has been the industry's standard dummy text ever since the 1500s, when an unknown printer took a galley of type and scrambled it to make a type specimen book. It has survived not only five centuries, but also the leap into electronic typesetting, remaining essentially unchanged.</p>

  <div class="divider"></div>

  <h2 class="section-title" style="left:707px;top:440px">Our Network Offers</h2>
  <div class="offer" style="top:493px">
    <div class="offer-thumb" role="img" aria-label="Businessman working at a computer"></div>
    <h3>Lorem Ipsum</h3>
    <p>Lorem Ipsum is simply dummy text of the print-ing and typesetting industry. Lorem Ipsum has been the industry's standard dummy text ever since the 1500s,</p>
  </div>
  <div class="offer" style="top:613px">
    <div class="offer-thumb" role="img" aria-label="Support agent with headset"></div>
    <h3>Lorem Ipsum</h3>
    <p>Lorem Ipsum is simply dummy text of the print-ing and typesetting industry. Lorem Ipsum has been the industry's standard dummy text ever since the 1500s,</p>
  </div>
  <div class="offer" style="top:738px">
    <div class="offer-thumb" role="img" aria-label="Team meeting around a laptop"></div>
    <h3>Lorem Ipsum</h3>
    <p>Lorem Ipsum is simply dummy text of the print-ing and typesetting industry. Lorem Ipsum has been industry's standard dummy text ever since the 1500s,</p>
  </div>

  <footer class="footer">
    <div class="footer-links">
      <a href="#">Home</a><span class="sep">|</span><a href="#">About Us</a><span class="sep">|</span><a href="#">Services</a><span class="sep">|</span><a href="#">Enquiry</a><span class="sep">|</span><a href="#">Contact us</a>
    </div>
    <div class="copyright">Copyright 2012.All rights reserved.</div>
  </footer>
</div>
</body>
</html>
```